K&R Security Services PTY. LTD.

Ive just had my logo made and I'm looking for some simple but strong designs for my business cards the company is a security company.

Please use dark colors.

Regards,

Owen Deloit

Reason: Need more time for discussion with other directors

Industry/Entity Type

Security

Font styles to use
Sans Serif
Decorative

```html
<!DOCTYPE html>
<html lang="en">
<head>
<meta charset="utf-8">
<title>K&amp;R Security Services – Business Card</title>
<link rel="stylesheet" href="https://fonts.googleapis.com/css2?family=Open+Sans:wght@400;600&family=Tinos&display=swap">
<style>
  :root {
    --stage: #141414;
    --card-black: #0c0c0c;
    --card-black-hi: #2a2a2a;
    --card-white: #f7f7f7;
    --band-grey: #cfcfcf;
    --ink: #1b1b1b;
    --ink-soft: #555555;
    --mark-light: #e6e6e6;
  }
  * { margin: 0; padding: 0; box-sizing: border-box; }
  html, body { width: 1200px; height: 900px; overflow: hidden; background: var(--stage); }
  .stage {
    width: 1200px; height: 900px;
    display: flex; flex-direction: column; align-items: center; justify-content: center;
    gap: 44px;
  }
  .card {
    position: relative; width: 560px; height: 320px;
    border-radius: 18px; overflow: hidden;
    box-shadow: 0 18px 40px rgba(0,0,0,.6);
  }

  /* Front */
  .card-front {
    background: linear-gradient(135deg, var(--card-black-hi) 0%, var(--card-black) 45%, #1c1c1c 70%, var(--card-black) 100%);
    display: flex; align-items: center; justify-content: center;
  }
  .brand { display: flex; align-items: center; gap: 14px; }
  .brand-square { width: 22px; height: 22px; background: currentColor; }
  .brand-name {
    font-family: "Open Sans", sans-serif; font-weight: 600;
    font-size: 56px; letter-spacing: 1px; line-height: 1;
  }
  .card-front .brand { color: var(--mark-light); }

  /* Back */
  .card-back { background: var(--card-black); }
  .card-back .shape { position: absolute; inset: 0; }
  .contact { position: absolute; left: 34px; top: 92px; color: var(--ink); }
  .contact-name { font-family: "Tinos", serif; font-size: 24px; line-height: 1.05; }
  .contact-title { font-family: "Tinos", serif; font-size: 15px; color: var(--ink-soft); margin-bottom: 12px; }
  .contact-list { list-style: none; font-family: "Open Sans", sans-serif; font-size: 14px; line-height: 1.45; }
  .contact-list li { display: flex; align-items: center; gap: 8px; min-height: 20px; }
  .contact-list .icon { width: 13px; height: 13px; flex: none; fill: var(--ink); }
  .contact-list .no-icon { width: 13px; flex: none; }
  .card-back .brand { position: absolute; right: 48px; top: 150px; color: var(--ink); }
  .card-back .brand-name { font-size: 40px; }
  .card-back .brand-square { width: 16px; height: 16px; }
</style>
</head>
<body>
<main class="stage">
  <section class="card card-front" aria-label="Card front">
    <div class="brand">
      <span class="brand-square"></span>
      <span class="brand-name">K&amp;R</span>
    </div>
  </section>

  <section class="card card-back" aria-label="Card back">
    <svg class="shape" viewBox="0 0 560 320" preserveAspectRatio="none" aria-hidden="true">
      <path d="M0,200 L560,200 L560,320 L0,320 Z" fill="var(--band-grey)"/>
      <path d="M0,72 C180,40 380,44 560,96 L560,268 C380,240 190,245 0,298 Z" fill="var(--card-white)"/>
    </svg>
    <div class="contact">
      <p class="contact-name">Your name Here</p>
      <p class="contact-title">Title Here</p>
      <ul class="contact-list">
        <li><span class="no-icon"></span>P.O. Box 7 Northvale Victoria 3100</li>
        <li><svg class="icon" viewBox="0 0 16 16"><path d="M3 1h3l1.5 4-2 1.2a9 9 0 0 0 4.3 4.3L11 8.5l4 1.5v3a2 2 0 0 1-2 2A12 12 0 0 1 1 3a2 2 0 0 1 2-2z"/></svg>(03) 95550148</li>
        <li><svg class="icon" viewBox="0 0 16 16"><path d="M4 0h8a1 1 0 0 1 1 1v14a1 1 0 0 1-1 1H4a1 1 0 0 1-1-1V1a1 1 0 0 1 1-1zm1 2v10h6V2zm3 11a1 1 0 1 0 0 2 1 1 0 0 0 0-2z"/></svg>0400555217</li>
        <li><svg class="icon" viewBox="0 0 16 16"><path d="M1 3h14v10H1zm1.5 1.5L8 9l5.5-4.5V4h-11z"/></svg>owen@northvalesec.net.au</li>
        <li><span class="no-icon"></span>K.R@northvalesec.net.au</li>
      </ul>
    </div>
    <div class="brand">
      <span class="brand-square"></span>
      <span class="brand-name">K&amp;R</span>
    </div>
  </section>
</main>
</body>
</html>
```